Keyvane - Premium Club Brochure

Up until now, we've used Canva to create the Brochure we have at-hand, the one attached to this enquiry.

I have been referred to DraftHive by my Business Partner, Marcus Penrovey.

We have recently established a New Real Estate Agency.

This Brochure is our Property Management Membership Brochure, describing the 3x Memberships (Gold, Platinum & Diamond) & outlining the Benefits & Bonuses that are included in these Memberships.

For ALL Pages, we are open to suggestions & other designs/templates/colour schemes.

Target Market(s)

Real Estate - Landlords / Investors

Industry/Entity Type

Real Estate

Font styles to use
Serif
Sans Serif

Colors

Designer to choose colors to be used in the design.

Requirements
Must have
• We would like to do the following:
• - Page 1:
• 1. Include under Email: info@keyvane-demo.com.au
• 2. Include Website under Email (www.keyvane-demo.com.au).
• Website
• www.keyvane-demo.com.au
• 3. The Picture on the right, could we change that Photo to a Block of Apartments & remove the Lines going across the Picture.
• - Page 2
• 1. Create a Border around the Page.
• 2. Heading - Make it stand out more.
• 3. Create Banners for 'Quality Service' & '2.5% Lowest Fees'.
• 4. Categorise the Memberships with these Boarders, please refer to the attachment for example.
• 5. Annual Savings - Make it stand out more.
• - Page 3
• - Page 4
• Please for ALL Fonts, make them the same, we do NOT have the correct font programs to unify them.
Nice to have
• - Page 1:
• Website
• www.keyvane-demo.com.au
• - Page 2:
• When it mentions "2.5% Lowest Fees', please feel free to provide any suggestions, we are open to any suggestions/ideas for this.
Should not have
• Grammar or Spelling errors.

```html
<!DOCTYPE html>
<html lang="en">
<head>
<meta charset="utf-8">
<title>Keyvane Group – Premium Membership Club</title>
<link href="https://fonts.googleapis.com/css2?family=Playfair+Display:wght@900&family=Roboto:wght@400;700&display=swap" rel="stylesheet">
<style>
  :root {
    --frame: #000000;
    --sunflower: #ffcc00;
    --paper: #ffffff;
    --ink: #111111;
    --gold-light: #f3d36a;
    --gold-dark: #a77a12;
    --silver-light: #f2f2f2;
    --silver-dark: #8a8a8a;
    --diamond-light: #ffffff;
    --diamond-dark: #9c9c9c;
  }
  * { margin: 0; padding: 0; box-sizing: border-box; }
  html, body { width: 857px; height: 1200px; overflow: hidden; background: var(--paper); }
  .brochure {
    position: relative;
    width: 857px;
    height: 1200px;
    border: 14px solid var(--frame);
    background: linear-gradient(to right, var(--sunflower) 0, var(--sunflower) 418px, var(--paper) 418px);
    font-family: "Roboto", Arial, sans-serif;
    color: var(--ink);
    overflow: hidden;
  }
  .club-title {
    position: absolute;
    top: 82px;
    left: 0;
    width: 100%;
    text-align: center;
    font-family: "Playfair Display", Georgia, serif;
    font-weight: 900;
    font-size: 49px;
    line-height: 68px;
    color: var(--ink);
  }
  .tier-badge {
    position: absolute;
    top: 248px;
    width: 166px;
    height: 162px;
    background: var(--sunflower);
  }
  .tier-badge__seal {
    position: absolute;
    inset: 6px;
    border-radius: 50%;
  }
  .tier-badge--gold { left: 88px; }
  .tier-badge--gold .tier-badge__seal { background: radial-gradient(circle at 40% 35%, var(--gold-light), var(--gold-dark)); }
  .tier-badge--platinum { left: 325px; }
  .tier-badge--platinum .tier-badge__seal { background: radial-gradient(circle at 40% 35%, var(--silver-light), var(--silver-dark)); }
  .tier-badge--diamond { left: 561px; }
  .tier-badge--diamond .tier-badge__seal { background: radial-gradient(circle at 40% 35%, var(--diamond-light), var(--diamond-dark)); }

  .benefits {
    position: absolute;
    top: 460px;
  }
  .benefits--management { left: 24px; width: 386px; }
  .benefits--sales { left: 428px; width: 392px; }
  .benefits__heading {
    text-align: center;
    font-weight: 700;
    font-size: 18px;
    line-height: 28px;
    margin-bottom: 8px;
    text-transform: uppercase;
  }
  .benefits__list {
    list-style: none;
    font-size: 19px;
    line-height: 27.5px;
  }
  .benefits__list li::before { content: "\2022\00a0"; }
</style>
</head>
<body>
  <main class="brochure">
    <h1 class="club-title">Keyvane Group<br>Premium Membership Club</h1>

    <div class="tier-badge tier-badge--gold" role="img" aria-label="Gold membership seal badge"><div class="tier-badge__seal"></div></div>
    <div class="tier-badge tier-badge--platinum" role="img" aria-label="Platinum membership seal badge"><div class="tier-badge__seal"></div></div>
    <div class="tier-badge tier-badge--diamond" role="img" aria-label="Diamond membership seal badge"><div class="tier-badge__seal"></div></div>

    <section class="benefits benefits--management">
      <h2 class="benefits__heading">Property Management Benefits:</h2>
      <ul class="benefits__list">
        <li>Discounted Property Management Fee/s.</li>
        <li>14-Days Rent Guarantee Assurance.</li>
        <li>Complimentary End-Of-Month Statement/s.</li>
        <li>Complimentary End-Of-Year Statements.</li>
        <li>Complimentary Outgoing-Payments Service.</li>
        <li>Complimentary Trade-Services Liaison.</li>
        <li>Complimentary Tribunal Representations.</li>
        <li>Complimentary Half-Yearly Inspections.</li>
        <li>Complimentary Half-Yearly Report with Photos.</li>
        <li>Complimentary Term Rent Review.</li>
        <li>Complimentary Landlord Insurance Liaison.</li>
        <li>Complimentary Depreciation Report Liaison.</li>
        <li>Complimentary Tax Gearing Calculation Guide.</li>
        <li>Complimentary Support to your Tax Agent/Accountant</li>
      </ul>
    </section>

    <section class="benefits benefits--sales">
      <h2 class="benefits__heading">Purchase &amp; Sales Benefits:</h2>
      <ul class="benefits__list">
        <li>“Cashback” Bonus on Purchase.</li>
        <li>Complimentary Legal Fee for Purchase.</li>
        <li>FREE Market Analysis Report.</li>
        <li>Complimentary Bank Valuation.</li>
        <li>Discounted Selling Fee.</li>
        <li>Complimentary Auctioneer Fee.</li>
        <li>FREE Mortgage Consultation.</li>
        <li>FREE Mortgage Loan Health Check.</li>
        <li>FREE 1st Home Buyer Consultation.</li>
        <li>FREE Wealth Creation in Property Investment Consultation.</li>
        <li>FREE Equity-Share Investment Advisory.</li>
        <li>FREE SMSF in Property Investment Consultation.</li>
        <li>Complimentary Property Investment Workshop.</li>
        <li>Complimentary Property Investment Seminar.</li>
      </ul>
    </section>
  </main>
</body>
</html>
```